KPV Construction we build lodges in Botswana

We need a Design Layout only with Categories where we can update each projects photos.... We have a web address and a host - kpv.construction

```html
<!DOCTYPE html>
<html lang="en">
<head>
<meta charset="utf-8">
<title>KPV Construction</title>
<link rel="stylesheet" href="https://fonts.googleapis.com/css2?family=Open+Sans:wght@400;600;700&family=Raleway:wght@400;600;700&display=swap">
<style>
:root{
  --blue:#2f7fc1;
  --navy:#0c3a66;
  --dark:#353535;
  --darker:#2b2b2b;
  --text:#555;
  --muted:#8a8a8a;
  --light:#f1f1f1;
  --white:#fff;
}
*{margin:0;padding:0;box-sizing:border-box}
html,body{width:1200px;height:3512px;overflow:hidden}
body{position:relative;background:var(--white);font-family:"Open Sans",sans-serif;color:var(--text);font-size:13px}
.abs{position:absolute}
h2,h3,.brand{font-family:"Raleway",sans-serif}

/* top bar */
.topbar{top:0;left:0;width:1200px;height:32px;background:var(--dark);color:#ccc;font-size:11px;display:flex;align-items:center;justify-content:space-between;padding:0 40px}
.topbar .contact{display:flex;gap:30px;align-items:center}
.topbar .contact span{display:flex;gap:6px;align-items:center}
.social{display:flex;gap:14px}
.social i{display:block;width:12px;height:12px;border-radius:50%;background:#bbb}

/* nav */
.nav{top:32px;left:0;width:1200px;height:88px;display:flex;align-items:center;justify-content:space-between;padding:0 40px}
.logo{display:flex;align-items:center;gap:10px;color:var(--navy);font-family:"Raleway",sans-serif;font-weight:700;font-size:18px}
.logo i{width:34px;height:34px;background:var(--navy);display:block}
.menu{display:flex;gap:44px;font-size:13px;color:#444;font-weight:600}
.menu a{position:relative;color:inherit;text-decoration:none}
.menu a.active::after{content:"";position:absolute;left:50%;bottom:-12px;width:5px;height:5px;margin-left:-2.5px;border-radius:50%;background:#333}

/* hero */
.hero{top:120px;left:0;width:1200px;height:620px;background:linear-gradient(180deg,#6f8fae 0%,#9fb4c8 45%,#d9e2ea 75%,#eef1f4 100%)}
.hero-cut{top:560px;left:0;width:1200px;height:180px}
.dots{top:656px;left:1020px;display:flex;gap:8px}
.dots i{width:10px;height:10px;border-radius:50%;background:var(--blue);display:block}
.dots i.on{background:none;border:2px solid var(--blue)}

/* welcome */
.welcome-kicker{top:778px;left:210px;font-size:15px;color:#333}
.welcome-title{top:800px;left:208px;font-size:34px;font-weight:600;color:var(--blue)}
.welcome-text{top:852px;left:210px;width:470px;line-height:1.6;font-size:13px}
.welcome-img{top:764px;left:732px;width:296px;height:300px;background:linear-gradient(135deg,#1d3e63,#6b8fb3 55%,#c8d6e3)}

/* about */
.about{top:1130px;left:0;width:1200px;height:570px;background:var(--light)}
.section-title{width:1200px;left:0;text-align:center;font-size:30px;font-weight:600;color:var(--blue)}
.section-title span{color:#333}
.about-img{top:1360px;left:152px;width:268px;height:262px;background:linear-gradient(160deg,#2a5a8a,#8fb2d4 60%,#d5e2ee)}
.card{top:1360px;height:262px;padding:34px 30px}
.card h3{font-size:24px;margin-bottom:20px}
.card p{font-size:11px;line-height:1.7}
.card-dark{left:448px;width:304px;background:var(--dark);color:#cfcfcf;height:290px}
.card-dark h3{color:var(--white)}
.card-light{left:780px;width:268px;background:#e6e6e6}
.card-light h3{color:var(--blue)}
.btn-sm{display:inline-block;margin-top:26px;border:1px solid #aaa;color:#eee;font-size:10px;padding:7px 16px}

/* projects */
.projects{top:1700px;left:0;width:1200px;height:890px;background:#ececec}
.tabs{top:1872px;left:0;width:1200px;display:flex;justify-content:center;gap:64px;font-size:12px;color:#666}
.tabs span.active{color:var(--blue);font-weight:600;border-bottom:2px solid var(--blue);padding-bottom:8px}
.tile{width:268px;height:216px}
.tile-dark{background:linear-gradient(160deg,#111,#3a3a3a);color:var(--white);padding:100px 24px 0}
.tile-dark h4{font-family:"Raleway",sans-serif;font-size:20px;line-height:1.2;font-weight:600}
.tile-dark p{font-size:11px;margin-top:12px;color:#ddd}
.btn-dark{top:2472px;left:552px;width:96px;height:32px;background:var(--dark);color:var(--white);font-size:11px;display:flex;align-items:center;justify-content:center}

/* contact */
.contact-panel{top:2590px;left:0;width:640px;height:480px;background:linear-gradient(180deg,#3e3e3e,#2c2c2c)}
.contact-title{top:2644px;left:144px;font-size:26px;font-weight:600;color:var(--white)}
.contact-title span{color:var(--blue)}
.field{left:144px;width:382px;height:36px;background:var(--white);border-radius:3px;font-size:11px;color:#888;padding:10px 12px}
.btn-blue{background:var(--blue);color:var(--white);font-size:11px;display:flex;align-items:center;justify-content:center}
.map{top:2590px;left:640px;width:560px;height:480px;background:linear-gradient(135deg,#e9e6df,#dcdad3 50%,#c9d9e8)}

/* footer */
.footer{top:3070px;left:0;width:1200px;height:320px;background:var(--navy);color:#c6d3e0}
.footer h3{font-size:20px;color:var(--white);margin-bottom:26px;font-weight:600}
.fcol{top:3112px}
.fcol ul{list-style:none;font-size:11px;line-height:2.6}
.fcol li::before{content:"\203A";margin-right:12px;color:#9fb4c8}
.info{display:flex;gap:16px;font-size:11px;line-height:1.5;margin-bottom:16px}
.info svg{flex:none;margin-top:2px}
.news-input{width:240px;height:30px;border-radius:15px;background:#3c6a96;margin:18px 0 14px}
.news-submit{display:flex;align-items:center;gap:10px;font-size:11px;color:var(--white)}
.news-submit i{width:14px;height:14px;border-radius:50%;background:var(--white);display:block}
.bottombar{top:3390px;left:0;width:1200px;height:122px;background:var(--dark);display:flex;align-items:center;justify-content:space-between;padding:0 120px;font-size:10px;color:#aaa}
.bottombar .social i{width:16px;height:16px}
</style>
</head>
<body>

<header class="topbar abs">
  <div class="contact">
    <span><svg width="11" height="11" viewBox="0 0 24 24"><path fill="#ccc" d="M6.6 10.8a15 15 0 0 0 6.6 6.6l2.2-2.2a1 1 0 0 1 1-.25 11 11 0 0 0 3.6.6 1 1 0 0 1 1 1V20a1 1 0 0 1-1 1A17 17 0 0 1 3 4a1 1 0 0 1 1-1h3.5a1 1 0 0 1 1 1c0 1.25.2 2.45.6 3.6a1 1 0 0 1-.25 1z"/></svg>(+267) 555 0148</span>
    <span><svg width="12" height="10" viewBox="0 0 24 18"><rect x="1" y="1" width="22" height="16" fill="none" stroke="#ccc" stroke-width="2"/><path d="M1 1l11 9 11-9" fill="none" stroke="#ccc" stroke-width="2"/></svg>info@kpv.construction</span>
  </div>
  <div class="social"><i></i><i></i><i></i></div>
</header>

<nav class="nav abs">
  <div class="logo"><i></i>KPV Construction</div>
  <div class="menu">
    <a class="active">Home</a><a>About Us</a><a>Our Projects</a><a>Contact Us</a>
  </div>
</nav>

<div class="hero abs" role="img" aria-label="High-rise towers under construction above the morning mist"></div>
<svg class="hero-cut abs" viewBox="0 0 1200 180" preserveAspectRatio="none"><polygon points="0,150 1200,40 1200,180 0,180" fill="#fff"/></svg>
<div class="dots abs"><i class="on"></i><i></i><i></i></div>

<section>
  <p class="welcome-kicker abs">Welcome to</p>
  <h1 class="welcome-title abs brand">KPV Construction</h1>
  <p class="welcome-text abs">Lorem Ipsum is simply dummy text of the printing and typesetting industry. Lorem Ipsum has been the industry's standard dummy text ever since the 1500s, when an unknown printer took a galley of type and scrambled it to make a type specimen book. It has survived not only five centuries, but also the leap into electronic typesetting, remaining essentially unchanged.</p>
  <div class="welcome-img abs" role="img" aria-label="Glass tower seen from below"></div>
</section>

<section class="about abs"></section>
<h2 class="section-title abs" style="top:1266px">About Us</h2>
<div class="about-img abs" role="img" aria-label="Blue glass office building facade"></div>
<div class="card card-dark abs">
  <h3>About Us</h3>
  <p>Lorem Ipsum is simply dummy text of the printing and typesetting industry. Lorem Ipsum has been the industry's standard dummy text ever since the 1500s, when an unknown printer took a galley of type and scrambled it to make a type specimen book from old text.</p>
  <span class="btn-sm">Read More</span>
</div>
<div class="card card-light abs">
  <h3>What we do</h3>
  <p>Lorem Ipsum is simply dummy text of the printing and typesetting industry. Lorem Ipsum has been the industry's standard dummy text ever since the 1500s, when a printer took a galley of type and scrambled it.</p>
</div>

<section class="projects abs"></section>
<h2 class="section-title abs" style="top:1780px"><span>Our</span> Projects</h2>
<div class="tabs abs"><span class="active">All Projects</span><span>Project 1</span><span>Project 2</span><span>Project 3</span><span>Project 4</span></div>
<div class="tile abs" style="top:1972px;left:172px;background:linear-gradient(160deg,#4d7fb0,#a9c4de 60%,#e4ecf4)" role="img" aria-label="Glass skyscraper against a blue sky"></div>
<div class="tile abs" style="top:1972px;left:464px;background:linear-gradient(160deg,#8fb8df,#d7e6f2 55%,#5d8a4a)" role="img" aria-label="White curved tower beside a tree"></div>
<div class="tile tile-dark abs" style="top:1972px;left:756px"><h4>Project Name<br>Goes Here</h4><p>Lorem ipsum is simply dummy text</p></div>
<div class="tile abs" style="top:2212px;left:172px;background:linear-gradient(180deg,#d8dde2,#eef0f2 55%,#7ea35c)" role="img" aria-label="White modern apartment block with balconies"></div>
<div class="tile abs" style="top:2212px;left:464px;background:linear-gradient(160deg,#2a2a2a,#8c8c8c 55%,#d0d0d0)" role="img" aria-label="Concrete building structure in shadow"></div>
<div class="tile abs" style="top:2212px;left:756px;background:linear-gradient(135deg,#0f3f7c,#3f86cf 55%,#9cc6ef)" role="img" aria-label="Blue glass tower corner"></div>
<div class="btn-dark abs">View All</div>

<section class="contact-panel abs" role="img" aria-label="Dark construction site backdrop"></section>
<h2 class="contact-title abs">Contact <span>Us</span></h2>
<div class="field abs" style="top:2716px">Your Name</div>
<div class="field abs" style="top:2760px">Your Email</div>
<div class="field abs" style="top:2804px">Subject</div>
<div class="field abs" style="top:2848px;height:86px">Message</div>
<div class="btn-blue abs" style="top:2954px;left:144px;width:80px;height:30px">Submit</div>
<div class="map abs" role="img" aria-label="City street map with the office location beside the river"></div>

<footer class="footer abs"></footer>
<div class="fcol abs" style="left:140px">
  <h3>Useful links</h3>
  <ul><li>Home</li><li>About Us</li><li>Our Projects</li><li>Contact Us</li></ul>
</div>
<div class="fcol abs" style="left:458px;width:260px">
  <h3>Contact Us</h3>
  <div class="info"><svg width="12" height="12" viewBox="0 0 24 24"><path fill="#c6d3e0" d="M6.6 10.8a15 15 0 0 0 6.6 6.6l2.2-2.2a1 1 0 0 1 1-.25 11 11 0 0 0 3.6.6 1 1 0 0 1 1 1V20a1 1 0 0 1-1 1A17 17 0 0 1 3 4a1 1 0 0 1 1-1h3.5a1 1 0 0 1 1 1c0 1.25.2 2.45.6 3.6a1 1 0 0 1-.25 1z"/></svg><div>Phone<br>(+267) 555 0148</div></div>
  <div class="info"><svg width="12" height="10" viewBox="0 0 24 18"><rect x="1" y="1" width="22" height="16" fill="none" stroke="#c6d3e0" stroke-width="2"/><path d="M1 1l11 9 11-9" fill="none" stroke="#c6d3e0" stroke-width="2"/></svg><div>Email<br>info@kpv.construction</div></div>
  <div class="info"><svg width="12" height="14" viewBox="0 0 24 30"><path fill="#c6d3e0" d="M12 0a10 10 0 0 0-10 10c0 8 10 20 10 20s10-12 10-20A10 10 0 0 0 12 0zm0 14a4 4 0 1 1 0-8 4 4 0 0 1 0 8z"/></svg><div>Address<br>Plot 214 Kgale View,<br>Gaborone, Botswana</div></div>
</div>
<div class="fcol abs" style="left:824px;width:260px">
  <h3>Newsletter</h3>
  <p style="font-size:11px;line-height:1.6">Lorem ipsum is simply dummy text of the printing and typesetting industry.</p>
  <div class="news-input"></div>
  <div class="news-submit"><i></i>Submit</div>
</div>

<div class="bottombar abs">
  <span>Copyright &copy; 2019 &middot; KPV Construction &middot; All rights reserved</span>
  <div class="social"><i></i><i></i><i></i></div>
</div>

</body>
</html>
```